Website for my photography business

I need a website for my photography business, Dana Lindqvist Photography. I need a website that has a landing page with a cover photo of each kind of photography I do. For example, Nature, Weddings, Portraits and Architecture. I want it so that when someone comes onto my website they have to choose which kind of photography page they want to visit. So if they click on the wedding photo it will open to a page with my wedding portfolio images and a contact me button. If they choose nature photography I want them to be redirected to an e-commerce section where they can purchase prints. Architecture and Portraits should open up to their respective portfolios with about me and contact info. I like this kind of format because I want people who come to my website for a specific type of photography to be able to be directed there easily without having to look at a mix of other kinds of photography. I will provide a few files to use as placeholders. I have already purchased the danalindqvistphotography.example domain name. A Wix website would be great because I am most familiar with it but I am open to anything.

Industry/Entity Type

Photographer

Number of Pages Required

5+ page

Requirements
Must have
• Landing Page and e-commerce

```html
<!DOCTYPE html>
<html lang="en">
<head>
<meta charset="utf-8">
<title>Dana Lindqvist Photography</title>
<link href="https://fonts.googleapis.com/css2?family=Poppins:wght@300;400;500&family=Playball&display=swap" rel="stylesheet">
<style>
:root{
  --night:#0c0e1f;
  --footer:#1a1b32;
  --ink:#272a5c;
  --text:#555;
  --white:#fff;
  --gold:#fbb03b;
  --script:"Playball",cursive;
  --sans:"Poppins",sans-serif;
}
*{margin:0;padding:0;box-sizing:border-box}
html,body{width:1200px;height:2760px;overflow:hidden}
body{position:relative;background:var(--white);font-family:var(--sans);color:var(--text)}
.abs{position:absolute}
.center{text-align:center;width:100%;left:0}

.hero{left:0;top:0;width:1200px;height:468px;background:var(--night)}
.brand{left:77px;top:34px;font-family:var(--sans);font-weight:300;font-size:18px;color:var(--white);letter-spacing:.5px}
.nav{top:36px;right:78px;display:flex;gap:30px;align-items:center;font-size:15px;color:var(--white)}
.nav a{color:var(--white);text-decoration:none}
.nav .active{color:var(--gold);position:relative}
.nav .active::after{content:"";position:absolute;left:0;bottom:-6px;width:20px;height:2px;background:var(--gold)}
.ring{left:957px;top:121px;width:48px;height:48px;border:9px solid var(--gold);border-radius:50%}
.dots-right{left:1103px;top:171px;width:97px;height:145px;background:radial-gradient(ellipse at right,rgba(251,176,59,.35),rgba(251,176,59,0) 70%)}
.dots-left{left:0;top:428px;width:80px;height:137px;background:linear-gradient(90deg,rgba(251,176,59,.25),rgba(251,176,59,.08))}
.welcome{left:80px;top:150px;font-size:82px;font-weight:400;color:var(--white);line-height:1}
.hero-title{left:82px;top:255px;font-family:var(--script);font-size:82px;color:var(--white);line-height:1.1}

.section-title{font-family:var(--script);font-size:46px;color:var(--ink);line-height:1}
.section-sub{font-size:14px;color:var(--text)}

.category{width:510px;height:386px;display:flex;align-items:center;justify-content:center;color:var(--white);font-size:24px}
.cat-wedding{left:77px;top:616px;background:linear-gradient(135deg,#b39266,#e4d2b4 55%,#c8a167)}
.cat-nature{left:613px;top:616px;background:linear-gradient(135deg,#7a6e64,#4a3a2e 55%,#8e8478)}
.cat-portraits{left:77px;top:1025px;background:linear-gradient(135deg,#2a140c,#5a3424 50%,#1a0b07)}
.cat-architecture{left:613px;top:1025px;background:linear-gradient(180deg,#516069,#3a4850 50%,#3b2520)}

.adventure{width:323px;height:291px;top:1590px}
.adv-1{left:94px;background:linear-gradient(180deg,#b8b79a,#8d8350 55%,#a4852f)}
.adv-2{left:438px;background:linear-gradient(180deg,#d7d3d4,#8a7260 50%,#4c5a2e)}
.adv-3{left:782px;background:linear-gradient(180deg,#2c3d33,#556248 50%,#e9eef2)}
.prints{top:1900px;font-family:var(--script);font-size:19px;color:var(--gold);text-decoration:underline}

.cta{left:0;top:2004px;width:1200px;height:323px;background:linear-gradient(180deg,#3a3c40,#25272b 60%,#2d2f33)}
.cta-title{top:2088px;font-family:var(--script);font-size:44px;color:var(--white);line-height:1}
.cta-sub{top:2147px;font-size:15px;color:var(--white)}
.cta-button{left:509px;top:2182px;width:181px;height:57px;background:var(--gold);border-radius:4px;color:var(--white);font-family:var(--script);font-size:22px;display:flex;align-items:center;justify-content:center}

.footer{left:0;top:2327px;width:1200px;height:433px;background:var(--footer);color:var(--white)}
.footer-col{top:2356px;width:260px;text-align:center}
.footer-col h3{font-family:var(--script);font-weight:400;font-size:23px;margin-bottom:18px}
.footer-col li{list-style:none;font-size:14.5px;line-height:27px}
.col-1{left:62px}.col-2{left:333px}.col-3{left:601px}.col-4{left:875px}
.newsletter p{font-size:14.5px;line-height:27px}
.email{left:879px;top:2470px;width:244px;height:46px;background:#f3f3f3;border-radius:4px;color:#666;font-size:14px;padding:0 17px;display:flex;align-items:center}
.subscribe{left:879px;top:2523px;width:244px;height:46px;background:var(--gold);border-radius:4px;font-family:var(--script);font-size:22px;color:var(--white);display:flex;align-items:center;justify-content:center}
.divider{left:77px;top:2611px;width:1046px;border-top:1px dotted #666}
.copyright{top:2652px;font-size:14.5px;color:var(--white)}
.social{top:2684px;width:46px;height:46px;border:1.5px solid var(--gold);border-radius:50%}
.social-1{left:556px}.social-2{left:609px}
</style>
</head>
<body>
<header class="abs hero"></header>
<div class="abs brand">Dana Lindqvist Photography</div>
<nav class="abs nav">
  <a class="active">Home</a><a>About Me</a><a>Photography</a><a>Contact</a>
  <svg width="20" height="20" viewBox="0 0 20 20" fill="none" stroke="#fff" stroke-width="1.5"><path d="M1 3h3l2.5 10h10l2-7H5"/><circle cx="8" cy="17" r="1.4"/><circle cx="15" cy="17" r="1.4"/></svg>
</nav>
<div class="abs ring"></div>
<div class="abs dots-right" role="img" aria-label="Gold dotted diamond decoration"></div>
<div class="abs dots-left" role="img" aria-label="Gold dotted grid decoration"></div>
<h1 class="abs welcome">Welcome to</h1>
<div class="abs hero-title">Dana Lindqvist Photography</div>

<h2 class="abs center section-title" style="top:505px">Photography</h2>
<p class="abs center section-sub" style="top:568px">Browse by Categories</p>

<a class="abs category cat-wedding" role="img" aria-label="Wedding rings on a lace pillow held in a hand">Wedding</a>
<a class="abs category cat-nature" role="img" aria-label="Brown bear standing among rocks">Nature</a>
<a class="abs category cat-portraits" role="img" aria-label="Close-up beauty portrait">Portraits</a>
<a class="abs category cat-architecture" role="img" aria-label="Round tower seen from below with a plane overhead">Architecture</a>

<h2 class="abs center section-title" style="top:1480px">latest Advanture</h2>
<p class="abs center section-sub" style="top:1537px">Nature Photography</p>

<div class="abs adventure adv-1" role="img" aria-label="Photographer with tripod on a misty hill"></div>
<div class="abs adventure adv-2" role="img" aria-label="Stone castle tower on a mossy cliff"></div>
<div class="abs adventure adv-3" role="img" aria-label="Red fox sitting in the snow"></div>
<a class="abs center prints">Purchase prints</a>

<section class="abs cta" role="img" aria-label="Dark lake pier with wooden posts and mountains"></section>
<h2 class="abs center cta-title">let's Create Some Magic</h2>
<p class="abs center cta-sub">Dana Lindqvist Photography</p>
<a class="abs cta-button">Contact Us</a>

<footer class="abs footer"></footer>
<div class="abs footer-col col-1"><h3>Sitemap</h3><ul><li>Home</li><li>About Me</li><li>Photography</li><li>Contact Us</li></ul></div>
<div class="abs footer-col col-2"><h3>My Account</h3><ul><li>My Account</li><li>Oredr History</li><li>Wishlist</li><li>Shopping Guide</li><li>Contact Us</li></ul></div>
<div class="abs footer-col col-3"><h3>Photography</h3><ul><li>Nature</li><li>Wedding</li><li>Portraits</li><li>Architecture</li></ul></div>
<div class="abs footer-col col-4 newsletter"><h3>Newsletter</h3><p>Receive our exclusive update<br>for signup!</p></div>
<div class="abs email">Enter Email *</div>
<div class="abs subscribe">Subscribe</div>
<div class="abs divider"></div>
<p class="abs center copyright">©Dana Lindqvist - 2020 All rights reserved.</p>
<a class="abs social social-1" aria-label="Social profile"></a>
<a class="abs social social-2" aria-label="Social profile"></a>
</body>
</html>
```